Loftvane.ca Your Canadian Source for all your mortgage needs.

I need to get a fresh look on my current website. It is not currently a Wordpress site and i need to build a whole new site that i can do my editing in using Wordpress.
I need it built in a mobile or responsive theme.
There will be a secured application page which is critical.
I have 3 books written so i want to be able to have advertising spaces for promoting them and a landing page ( I can build my own landing pages)
I need the frame work of a professional theme with easy editing capabilities.
I have my own LOGOs which i would continue to use. The current site can be reviewed at www.loftvane.ca.
The front page could have a young couple near a nice house, open to suggestions.
I don't need a blog post to update but if it was on the sides of the pages I could use it. Something like a "Latest News" section.
I would like to have a Main page, Application Page, Resource page, Contact page, Calculator Page, a questions and answer page. Theses can be populated with the current information or I can add latter.
I want the main page to be a mini sales page so I can link to Posts on First Time Home Buyers, Refinance Options, Second Home or New purchase options.
I provide mortgages for people across Canada so i want the Canadian Flag incorporated
I like the colors to work with the logo colors on the current site

Target Market(s)

Canadian Mortgage Clients

Font styles to use
Sans Serif

Colors
3277b5
cadf82

Requirements
Must have
• Must work in a Wordpress Theme
• Please see Project description for more details
Nice to have
• Space to add banner ads for my books. I have 3 books written

```html
<!DOCTYPE html>
<html lang="en">
<head>
<meta charset="utf-8">
<title>Loftvane.ca – Your Canadian Source for Mortgages</title>
<link href="https://fonts.googleapis.com/css2?family=Open+Sans:wght@400;600;700&family=Oswald:wght@400;500;700&display=swap" rel="stylesheet">
<style>
:root{
  --blue:#3277b5;
  --blue-dark:#1f4f7d;
  --navy:#173a5c;
  --navy-deep:#10283f;
  --green:#a9c84a;
  --green-light:#cadf82;
  --ink:#2b2b2b;
  --muted:#6d6d6d;
  --grey-bg:#efefef;
  --line:#dcdcdc;
  --red:#d52b1e;
  --white:#fff;
}
*{box-sizing:border-box;margin:0;padding:0}
html,body{width:1200px;height:2592px;overflow:hidden}
body{font-family:"Open Sans",Arial,sans-serif;color:var(--ink);background:var(--white);font-size:15px;line-height:1.6}
h1,h2,h3,h4,.cond{font-family:"Oswald","Arial Narrow",sans-serif}
.wrap{width:1040px;margin:0 auto;position:relative}
.btn{display:inline-block;background:var(--green);color:var(--white);font-size:13px;font-weight:600;padding:6px 18px;border-radius:3px}

/* header */
.site-header{height:88px}
.site-header .wrap{display:flex;justify-content:space-between;align-items:center;height:88px}
.brand{display:flex;align-items:center;gap:12px;font-weight:700;font-size:34px;color:var(--blue);letter-spacing:-.5px}
.brand-mark{width:22px;height:22px;background:var(--green)}
.header-contact{display:flex;align-items:center;gap:16px}
.phone-block{text-align:right;line-height:1.2}
.phone-block small{display:block;font-size:11px;color:var(--muted);letter-spacing:1px}
.phone-block strong{font-size:24px;color:var(--ink)}
.flag{width:44px;height:26px;display:flex;border:1px solid var(--line)}
.flag span{flex:1;background:var(--red)}
.flag span:nth-child(2){flex:2;background:var(--white)}
.main-nav{height:32px;background:var(--white);border-top:1px solid var(--line)}
.main-nav ul{list-style:none;display:flex;gap:0}
.main-nav li{font-size:14px;font-weight:700;color:var(--blue-dark);padding:5px 18px;text-transform:uppercase}
.main-nav li.active{background:var(--green);color:var(--white)}

/* hero */
.hero{height:540px;position:relative;background:linear-gradient(180deg,#9fc3e4 0%,#c9dcea 40%,#7d8c6a 80%,#5d6f47 100%)}
.hero-photo{position:absolute;inset:0}
.hero-caption{position:absolute;right:80px;bottom:50px;width:520px;background:rgba(20,30,40,.75);color:var(--white);padding:22px 28px}
.hero-caption h1{font-size:38px;font-weight:700;line-height:1.1;text-transform:uppercase}
.hero-caption p{font-family:"Oswald",sans-serif;font-size:20px;text-transform:uppercase;line-height:1.25;margin-top:6px}

/* why */
.why{background:var(--grey-bg);height:280px;text-align:center;padding-top:40px}
.why h2{font-size:28px;font-weight:500;color:#333;text-transform:uppercase}
.why p{font-size:13px;color:var(--muted);margin:14px auto 0;width:900px}
.why .btn{margin-top:22px}

/* features */
.features{padding-top:40px;height:340px}
.features .wrap{display:flex;justify-content:space-between}
.feature{width:320px;background:var(--grey-bg);text-align:center;padding:64px 24px 22px;position:relative;height:260px}
.feature-icon{position:absolute;top:-34px;left:50%;transform:translateX(-50%);width:78px;height:78px;border-radius:50%;background:var(--blue);border:5px solid var(--white);display:flex;align-items:center;justify-content:center}
.feature h3{font-size:18px;font-weight:700;color:#333;text-transform:uppercase;line-height:1.15}
.feature p{font-size:13px;color:var(--muted);margin:10px 0 14px}

/* books */
.books{height:300px}
.books .wrap{display:flex;justify-content:space-between}
.book-ad{width:320px;height:260px;background:linear-gradient(135deg,#7a5a33,#a47a47 55%,#6b4a28)}
.book-ad.green{background:linear-gradient(135deg,#6e5131,#a07a48 50%,#5c7d3a)}
.book-ad.warm{background:linear-gradient(135deg,#7d5a32,#b48950 55%,#6a4726)}

/* lower */
.lower .wrap{display:flex;justify-content:space-between}
.lower-left{width:600px}
.testimonials{text-align:center}
.testimonials h2{font-size:26px;font-weight:500;text-transform:uppercase;display:flex;align-items:center;gap:16px;justify-content:center}
.testimonials h2::before,.testimonials h2::after{content:"";flex:1;height:1px;background:var(--line)}
.quote-badge{width:50px;height:50px;border-radius:50%;background:var(--green);color:var(--white);font-size:36px;font-family:Georgia,serif;line-height:64px;margin:22px auto 14px}
.testimonials blockquote{font-size:14px;font-style:italic;color:var(--muted);text-align:left;padding:0 10px}
.reviewer{display:flex;align-items:center;gap:10px;margin:16px 10px 0;text-align:left}
.reviewer-avatar{width:44px;height:44px;border-radius:50%;background:#b8c3cc}
.reviewer strong{display:block;font-size:13px}
.reviewer small{font-size:11px;color:var(--muted)}
.auction{margin-top:50px;background:var(--green-light);padding:26px 40px;text-align:center;height:160px}
.auction h3{font-size:28px;font-weight:500;color:var(--blue-dark);text-transform:uppercase}
.auction p{font-size:12px;color:#556;margin-top:2px}
.subscribe{display:flex;justify-content:center;margin-top:14px}
.subscribe span{width:320px;height:36px;background:var(--white);font-size:12px;color:#999;padding:8px 12px;text-align:left}
.subscribe b{background:var(--navy-deep);color:var(--white);font-size:13px;padding:8px 18px}

.question-form{width:400px;background:var(--navy-deep);color:var(--white);padding:20px 26px;height:540px}
.question-form h2{font-size:26px;font-weight:500;text-transform:uppercase;text-align:center;margin-bottom:14px}
.question-form label{display:block;font-size:12px;font-weight:600;margin-top:8px}
.field{background:var(--white);height:34px;font-size:12px;color:#999;padding:7px 10px;margin-top:4px}
.field-row{display:flex;gap:12px}
.field-row .field{flex:1}
.field.tall{height:120px}
.submit{margin-top:18px;background:var(--green);text-align:center;font-family:"Oswald",sans-serif;font-size:22px;padding:6px 0}

/* cta band */
.cta-band{position:absolute;top:2220px;left:0;width:1200px;height:100px;background:var(--blue);color:var(--white)}
.cta-band .wrap{display:flex;align-items:center;height:100px;justify-content:space-between}
.cta-title{font-family:"Oswald",sans-serif;font-size:24px;line-height:1.05;text-transform:uppercase;color:var(--green-light)}
.cta-item{display:flex;align-items:center;gap:10px;font-size:12px;line-height:1.3;text-transform:uppercase}
.cta-item strong{display:block;font-size:14px}
.cta-icon{width:36px;height:36px;border-radius:50%;border:2px solid var(--white);display:flex;align-items:center;justify-content:center}

/* footer */
.site-footer{position:absolute;top:2320px;left:0;width:1200px;height:220px;background:var(--navy);color:#c7d4e0;font-size:12px}
.site-footer .wrap{display:flex;justify-content:space-between;padding-top:26px}
.footer-col{width:230px}
.footer-col h4{font-family:"Open Sans",sans-serif;font-size:13px;color:var(--white);font-weight:600;margin-bottom:10px}
.footer-col li{list-style:none}
.news-item{margin-bottom:10px}
.news-item small{color:#8fa7bd;display:block}
.socials{display:flex;gap:8px}
.socials span{width:30px;height:30px;border-radius:50%;background:var(--blue)}
.copyright{position:absolute;top:2540px;left:0;width:1200px;height:52px;background:var(--navy-deep);color:#8fa7bd;font-size:11px;text-align:center;line-height:52px}
</style>
</head>
<body>

<header class="site-header">
  <div class="wrap">
    <div class="brand"><span class="brand-mark"></span>Loftvane</div>
    <div class="header-contact">
      <div class="phone-block"><small>CONTACT US</small><strong>403-555-0142</strong></div>
      <div class="flag" aria-label="Canadian colours"><span></span><span></span><span></span></div>
    </div>
  </div>
</header>
<nav class="main-nav">
  <div class="wrap">
    <ul>
      <li class="active">Home</li><li>Application</li><li>Resource</li><li>Calculator</li><li>FAQs</li><li>Contact Us</li>
    </ul>
  </div>
</nav>

<section class="hero">
  <div class="hero-photo" role="img" aria-label="Smiling young couple standing in front of a grey two-storey house"></div>
  <div class="hero-caption">
    <h1>Customize Your Mortgage</h1>
    <p>And learn how to save thousands of dollars on your current or next mortgage</p>
  </div>
</section>

<section class="why">
  <h2>Why Use a Mortgage Broker?</h2>
  <p>Professional representation for you and your family to help negotiate one of your biggest investments in your life. Helping you plan your mortgage to save you the most money.</p>
  <p>Learn about our "Mortgage Action Plan" which helps you tailor your mortgage to fit your family's needs. Teaching you how to save thousands on your mortgage and allowing you to be mortgage free years sooner than planned.</p>
  <span class="btn">Read more</span>
</section>

<section class="features">
  <div class="wrap">
    <article class="feature">
      <div class="feature-icon"><svg width="34" height="34" viewBox="0 0 24 24" fill="none" stroke="#fff" stroke-width="2"><circle cx="12" cy="8" r="4"/><path d="M4 21c0-4 4-6 8-6s8 2 8 6"/></svg></div>
      <h3>Apply Online Now!</h3>
      <p>We listen to the needs of our clients to get you a rate that suits your plans.</p>
      <span class="btn">Click Here</span>
    </article>
    <article class="feature">
      <div class="feature-icon"><svg width="34" height="34" viewBox="0 0 24 24" fill="none" stroke="#fff" stroke-width="2"><rect x="5" y="3" width="14" height="18" rx="1"/><path d="M8 8h8M8 12h8M8 16h5"/></svg></div>
      <h3>Save Thousands<br>on Your Mortgage</h3>
      <p>Customize your next mortgage to fit your financial needs.</p>
      <span class="btn">Free PDF Document</span>
    </article>
    <article class="feature">
      <div class="feature-icon"><svg width="34" height="34" viewBox="0 0 24 24" fill="none" stroke="#fff" stroke-width="2"><rect x="5" y="3" width="14" height="18" rx="1"/><rect x="8" y="6" width="8" height="3"/><path d="M8 13h1M12 13h1M15 13h1M8 17h1M12 17h1M15 17h1"/></svg></div>
      <h3>Mortgage<br>Calculators</h3>
      <p>Work out your payments and compare options quickly.</p>
      <span class="btn">Click Here</span>
    </article>
  </div>
</section>

<section class="books">
  <div class="wrap">
    <div class="book-ad" role="img" aria-label="Book cover advertisement: a guide for first time home buyers, on a wooden background"></div>
    <div class="book-ad green" role="img" aria-label="Book cover advertisement: a green mortgage savings guide, on a wooden background"></div>
    <div class="book-ad warm" role="img" aria-label="Book cover advertisement: how to save thousands on your mortgage, on a wooden background"></div>
  </div>
</section>

<section class="lower">
  <div class="wrap">
    <div class="lower-left">
      <div class="testimonials">
        <h2>What Our Clients Say</h2>
        <div class="quote-badge">&ldquo;</div>
        <blockquote>"Working with this team was simple from start to finish. They explained every option clearly, found us a better rate than our bank offered, and set up a payment plan that will have our home paid off years earlier than we expected."</blockquote>
        <div class="reviewer"><span class="reviewer-avatar"></span><div><strong>Dana Whitfield</strong><small>First time home buyer</small></div></div>
      </div>
      <div class="auction">
        <h3>Auction Alerts!</h3>
        <p>Sign up and be the first to hear about new property auctions.</p>
        <div class="subscribe"><span>Enter your email here</span><b>Subscribe</b></div>
      </div>
    </div>

    <form class="question-form">
      <h2>Do You Have a Question?</h2>
      <label>Your Name*</label>
      <div class="field-row"><div class="field">First Name</div><div class="field">Last Name</div></div>
      <label>Email*</label>
      <div class="field">Your Email Address here</div>
      <label>Phone</label>
      <div class="field">Phone Number</div>
      <label>Comments*</label>
      <div class="field tall"></div>
      <div class="submit">SUBMIT</div>
    </form>
  </div>
</section>

<section class="cta-band">
  <div class="wrap">
    <div class="cta-title">Have<br>Questions?</div>
    <div class="cta-item"><span class="cta-icon"><svg width="16" height="16" viewBox="0 0 24 24" fill="#fff"><path d="M6 2l4 4-2 3c1 3 4 6 7 7l3-2 4 4-3 4C10 22 2 14 2 5z"/></svg></span><div>Call us<strong>403-555-0142</strong></div></div>
    <div class="cta-item"><span class="cta-icon"><svg width="16" height="16" viewBox="0 0 24 24" fill="none" stroke="#fff" stroke-width="2"><rect x="3" y="5" width="18" height="14"/><path d="M3 5l9 8 9-8"/></svg></span><div>Send us<strong>an email</strong></div></div>
    <div class="cta-item"><span class="cta-icon"><svg width="16" height="16" viewBox="0 0 24 24" fill="#fff"><path d="M12 2a7 7 0 0 0-7 7c0 5 7 13 7 13s7-8 7-13a7 7 0 0 0-7-7zm0 10a3 3 0 1 1 0-6 3 3 0 0 1 0 6z"/></svg></span><div>Find a<strong>local office</strong></div></div>
    <div class="cta-item"><span class="cta-icon"><svg width="16" height="16" viewBox="0 0 24 24" fill="none" stroke="#fff" stroke-width="2"><path d="M4 4h7v16H4zM13 4h7v16h-7z"/></svg></span><div>Read the<strong>FAQs</strong></div></div>
  </div>
</section>

<footer class="site-footer">
  <div class="wrap">
    <div class="footer-col">
      <h4>Contact Us</h4>
      <p>Loftvane Mortgages Inc.<br>210, 880 Harbour Rise SW<br>Calgary, Alberta T2X 0K4<br>www.loftvane.ca</p>
    </div>
    <div class="footer-col">
      <h4>Latest News</h4>
      <div class="news-item"><small>January 10, 2015</small>New spring rates announced for fixed terms</div>
      <div class="news-item"><small>January 10, 2015</small>Tips for renewing your mortgage early</div>
    </div>
    <div class="footer-col">
      <h4>Quick links</h4>
      <ul><li>Home</li><li>Application</li><li>Resource</li><li>Calculator</li><li>FAQs</li><li>Contact Us</li></ul>
    </div>
    <div class="footer-col">
      <h4>Connect with us</h4>
      <div class="socials"><span></span><span></span><span></span></div>
    </div>
  </div>
</footer>
<div class="copyright">© 2015 Loftvane Mortgages. All Rights Reserved &nbsp;•&nbsp; Terms and Conditions &nbsp;•&nbsp; Privacy Policy &nbsp;•&nbsp; Terms of Use</div>

</body>
</html>
```